Label Craft Beer with CBD

Create a label for our cbd (cannabidiol) beer. We do have a first / simple idea. now it needs a professional finish. Please show your very own idea as well, because ours is only a draft and we need YOUR HELP! size front: H 8 cm, W 7 cm size back: H 7.5 cm, W 5.5 cm

```html
<!DOCTYPE html>
<html lang="en">
<head>
<meta charset="utf-8">
<title>Verda Brew – Premium Lager Label</title>
<link rel="stylesheet" href="https://fonts.googleapis.com/css2?family=Alfa+Slab+One&family=Roboto+Slab:wght@400;700&display=swap">
<style>
  :root {
    --bark: #2c2018;
    --moss: #4c5a2d;
    --moss-dark: #3e4a24;
    --paper: #ffffff;
    --ink: #262220;
    --ring: #6b3f22;
    --silver: #b9b9b1;
  }
  * { margin: 0; padding: 0; box-sizing: border-box; }
  html, body { width: 1050px; height: 1200px; overflow: hidden; background: var(--bark); }
  .label {
    position: relative;
    width: 1050px;
    height: 1200px;
    overflow: hidden;
    background: var(--bark);
    font-family: "Roboto Slab", Georgia, serif;
    color: var(--paper);
  }
  .contour-field {
    position: absolute; inset: 0;
    background: radial-gradient(ellipse at 40% 45%, #33261c 0%, var(--bark) 70%);
  }
  .base-wave { position: absolute; left: 0; top: 0; width: 1050px; height: 1200px; }

  .badge { position: absolute; width: 120px; height: 138px; }
  .badge polygon { fill: none; stroke: var(--paper); stroke-width: 2.5; }
  .badge text {
    fill: var(--paper);
    font-family: "Roboto Slab", Georgia, serif;
    font-size: 26px;
    text-anchor: middle;
  }
  .badge.small text { font-size: 22px; }
  .badge--well { left: 114px; top: 74px; }
  .badge--thc { left: 816px; top: 58px; }
  .badge--cbd { left: 27px; top: 1024px; }
  .badge--hangover { left: 166px; top: 1024px; }
  .badge--alc { left: 759px; top: 1024px; }
  .badge--volume { left: 899px; top: 1024px; }

  .name-band {
    position: absolute;
    top: 276px; height: 106px;
    background: var(--paper);
    color: var(--ink);
    font-family: "Alfa Slab One", Georgia, serif;
    font-size: 60px;
    letter-spacing: 2px;
    display: flex; align-items: center; justify-content: center;
  }
  .name-band--left { left: 0; width: 330px; padding-right: 10px; }
  .name-band--right { left: 700px; width: 350px; padding-left: 20px; }

  .brand-seal {
    position: absolute;
    left: 336px; top: 140px;
    width: 376px; height: 376px;
    border-radius: 50%;
    background: var(--paper);
    display: flex; align-items: center; justify-content: center;
  }
  .brand-seal__name {
    font-family: "Alfa Slab One", Georgia, serif;
    font-size: 46px;
    color: var(--ring);
    text-align: center;
    line-height: 1.15;
    letter-spacing: 3px;
  }

  .product-type {
    position: absolute; left: 0; width: 1050px; top: 553px;
    text-align: center;
    font-family: "Alfa Slab One", Georgia, serif;
    font-size: 43px;
    letter-spacing: 1px;
  }
  .product-style {
    position: absolute; left: 0; width: 1050px; top: 640px;
    text-align: center;
    font-family: "Alfa Slab One", Georgia, serif;
    font-size: 28px;
    letter-spacing: 1px;
  }

  .origin-mark {
    position: absolute; left: 0; width: 1050px; top: 1090px;
    display: flex; align-items: center; justify-content: center; gap: 10px;
    font-family: "Alfa Slab One", Georgia, serif;
    font-size: 22px;
    letter-spacing: 1px;
  }
  .origin-mark svg { width: 32px; height: 32px; }
</style>
</head>
<body>
<main class="label">
  <div class="contour-field" role="img" aria-label="Fine topographic contour line pattern on dark brown"></div>

  <svg class="base-wave" viewBox="0 0 1050 1200" aria-hidden="true">
    <defs>
      <linearGradient id="swoosh" x1="0" y1="0" x2="1" y2="0">
        <stop offset="0" stop-color="#ffffff"/>
        <stop offset="0.35" stop-color="#cfcfc6"/>
        <stop offset="0.6" stop-color="#ffffff"/>
        <stop offset="0.85" stop-color="#9a9a8e"/>
        <stop offset="1" stop-color="#e6e6df"/>
      </linearGradient>
    </defs>
    <path d="M0,950 C330,940 640,800 1050,782 L1050,880 C640,880 330,965 0,985 Z" fill="url(#swoosh)"/>
    <path d="M0,982 C330,962 640,872 1050,870 L1050,888 C640,890 330,978 0,996 Z" fill="#ffffff"/>
    <path d="M0,994 C330,976 640,886 1050,886 L1050,1200 L0,1200 Z" fill="var(--moss)"/>
  </svg>

  <svg class="badge badge--well" viewBox="0 0 120 138">
    <polygon points="60,3 116,35 116,103 60,135 4,103 4,35"/>
    <text x="60" y="64">WELL</text>
    <text x="60" y="96">BEING</text>
  </svg>
  <svg class="badge badge--thc" viewBox="0 0 120 138">
    <polygon points="60,3 116,35 116,103 60,135 4,103 4,35"/>
    <text x="60" y="64">NO</text>
    <text x="60" y="96">THC</text>
  </svg>

  <div class="name-band name-band--left">VERDA</div>
  <div class="name-band name-band--right">BREW</div>

  <div class="brand-seal">
    <div class="brand-seal__name">LORIVAL<br>ALPINE</div>
  </div>

  <div class="product-type">PREMIUM LAGER</div>
  <div class="product-style">NATURTRÜB</div>

  <svg class="badge badge--cbd" viewBox="0 0 120 138">
    <polygon points="60,3 116,35 116,103 60,135 4,103 4,35"/>
    <text x="60" y="64">10 MG</text>
    <text x="60" y="96">CBD</text>
  </svg>
  <svg class="badge small badge--hangover" viewBox="0 0 120 138">
    <polygon points="60,3 116,35 116,103 60,135 4,103 4,35"/>
    <text x="60" y="50">NO</text>
    <text x="60" y="76">HANG</text>
    <text x="60" y="102">OVER</text>
  </svg>

  <div class="origin-mark">
    <span>SWISS</span>
    <svg viewBox="0 0 32 32" aria-hidden="true">
      <rect x="1" y="1" width="30" height="30" rx="6" fill="#ffffff"/>
      <path d="M13,6 H19 V13 H26 V19 H19 V26 H13 V19 H6 V13 H13 Z" fill="var(--moss)"/>
    </svg>
    <span>MADE</span>
  </div>

  <svg class="badge badge--alc" viewBox="0 0 120 138">
    <polygon points="60,3 116,35 116,103 60,135 4,103 4,35"/>
    <text x="60" y="64">4.3%</text>
    <text x="60" y="96">ALC</text>
  </svg>
  <svg class="badge badge--volume" viewBox="0 0 120 138">
    <polygon points="60,3 116,35 116,103 60,135 4,103 4,35"/>
    <text x="60" y="64">330</text>
    <text x="60" y="96">CL</text>
  </svg>
</main>
</body>
</html>
```